Bright Harbor Capital website

Build a website template for the Bright Harbor Capital fund.
Looking for a cool website design showing companies we are using the latest in web design trends. We want to attract app developers, typically the younger set.
A good example of one of our competitive firms is http://mossfinch.org
The required components for the website include:
1) Funding application
2) about our firm
a) Partner profiles - We will include photographs and bios about each of the partners in our firm.
b) Invest with Bright Harbor - This will include information how to invest with our fund
c) our process - About our process for evaluating, funding and helping build successful businesses - This will include a narrative about the target companies, how we work, the type of deals we are interested in, our expectations, etc ...
3) Investment profiles - Stories about the companies we invest with
4) News - Output from our twitter feed and copies of our Blog posts

```html
<!DOCTYPE html>
<html lang="en">
<head>
<meta charset="utf-8">
<title>Bright Harbor Capital</title>
<link href="https://fonts.googleapis.com/css2?family=Open+Sans:wght@300;400;600;700&family=Kaushan+Script&display=swap" rel="stylesheet">
<style>
:root{
  --green:#5b9c12;
  --green-dark:#4a8409;
  --green-text:#5a9a17;
  --ink:#333;
  --muted:#777;
  --orange:#f08a12;
  --orange-light:#f7a32a;
  --header-bg:#f7f7f7;
  --footer-bg:#141414;
  --field:#e6e6e6;
}
*{box-sizing:border-box;margin:0;padding:0}
html,body{width:706px;height:1200px;overflow:hidden}
body{position:relative;background:#fff;font-family:"Open Sans",Arial,sans-serif;color:var(--ink)}
.abs{position:absolute}

.site-header{left:0;top:0;width:706px;height:64px;background:var(--header-bg)}
.brand{left:66px;top:18px;display:flex;align-items:center;gap:7px}
.brand-mark{width:22px;height:22px;border-radius:50%;background:var(--green)}
.brand-name{font-size:20px;font-weight:700;color:var(--green)}
.call{right:70px;top:20px;text-align:right;line-height:1.1}
.call strong{display:block;font-weight:400;font-size:13px;color:#222}
.call span{font-size:10px;color:#222}

.main-nav{left:0;top:64px;width:706px;height:26px;background:linear-gradient(#66a818,var(--green-dark))}
.nav-list{left:66px;top:-3px;display:flex;list-style:none;height:32px;align-items:center}
.nav-list li{font-size:7.6px;color:#fff;padding:0 10px;border-right:1px solid rgba(0,0,0,.18);line-height:14px}
.nav-list li:last-child{border:none}
.nav-list li.active{background:#2a2a2a;height:32px;line-height:32px;padding:0 6px;font-size:7.4px}

.hero{left:0;top:90px;width:706px;height:274px;background:linear-gradient(90deg,#e9e9e9 0%,#dcdcdc 45%,#c9c9c9 100%);overflow:hidden}
.hero-photo{left:328px;top:0;width:378px;height:274px;background:radial-gradient(ellipse at 65% 45%,#f4f2ef 0%,#d8d6d2 55%,#bcbcbc 100%)}
.hero-title{left:67px;top:64px;font-size:25px;font-weight:700;line-height:27px;color:#2b2b2b}
.hero-text{left:67px;top:135px;width:260px;font-size:10px;line-height:12.5px;color:#333}
.hero-btn{left:66px;top:194px;width:142px;height:29px;background:linear-gradient(var(--orange-light),var(--orange));border-radius:2px;color:#fff;font-size:10px;display:flex;align-items:center;padding-left:10px;gap:12px}
.hero-btn svg{flex:none}

.tagline{left:0;top:384px;width:706px;text-align:center;font-size:14.5px;font-weight:300;line-height:19px;color:#444}
.tagline b{font-weight:400;color:var(--green-text)}

.route{left:0;top:440px}
.route-label{font-size:9.5px;color:var(--green-text);text-align:center;width:120px}

.divider{left:66px;top:746px;width:604px;height:1px;background:#ececec}

.section-title{font-size:16px;font-weight:300;color:#333}
.post{width:140px}
.post-head{display:flex;gap:6px}
.post-date{width:18px;text-align:center}
.post-date .day{display:block;background:#eee;font-size:10.5px;color:#555;height:22px;line-height:22px}
.post-date .mon{display:block;background:var(--green);color:#fff;font-size:6.5px;height:9px;line-height:9px}
.post-title{font-size:11px;line-height:14px;color:#666;font-weight:300;width:110px}
.post-body{margin-top:13px;font-size:8.6px;line-height:11.8px;color:#777}

.request{left:438px;top:790px;width:190px;height:171px;border:1px solid #e2e2e2;padding:4px}
.field{background:var(--field);border-radius:2px;font-size:7.8px;color:#444;padding:6px 7px;height:23px;margin-bottom:4px}
.field.msg{height:81px}
.submit{width:60px;height:21px;background:#222;color:#fff;font-size:9px;font-weight:700;display:flex;align-items:center;justify-content:center;border-radius:2px}

.site-footer{left:0;top:1010px;width:706px;height:190px;background:var(--footer-bg);color:#fff}
.tab{left:68px;top:-10px;width:82px;height:22px;background:var(--green);font-family:"Kaushan Script",cursive;font-size:11px;display:flex;align-items:center;justify-content:center}
.foot-title{font-size:13px;font-weight:300}
.foot-links{list-style:none;font-size:7.6px;line-height:12.4px;margin-top:8px}
.tweet{display:flex;gap:6px;margin-top:8px}
.tweet-icon{width:20px;height:20px;background:#fff;flex:none;display:flex;align-items:center;justify-content:center}
.tweet-icon i{width:10px;height:10px;border-radius:50%;background:var(--green)}
.tweet p{font-size:7.4px;line-height:11.8px;width:108px}
.contact-list{list-style:none;font-size:7.4px;color:#8a8a8a;margin-top:8px}
.contact-list li{display:flex;align-items:center;gap:4px;margin-bottom:9px}
.contact-list b{font-weight:600;color:#9a9a9a}
.contact-list .mail{color:#fff}
.foot-rule{left:70px;top:154px;width:526px;height:1px;background:#2a2a2a}
.copyright{left:0;top:168px;width:706px;text-align:center;font-size:7.4px;color:#ccc}
</style>
</head>
<body>

<header class="site-header abs">
  <div class="brand abs"><span class="brand-mark"></span><span class="brand-name">Bright Harbor</span></div>
  <div class="call abs"><strong>Call us today!</strong><span>(123) 456-7890</span></div>
</header>

<nav class="main-nav abs">
  <ul class="nav-list abs">
    <li class="active">HOME</li>
    <li>About Our firm</li>
    <li>Funding Application</li>
    <li>Invest with Bright Harbor</li>
    <li>Our Process</li>
    <li>Investment Profiles</li>
    <li>Partner Profiles</li>
    <li>Contact Us</li>
  </ul>
</nav>

<section class="hero abs">
  <div class="hero-photo abs" role="img" aria-label="Smiling businessman in a white shirt and tie gesturing towards the headline in a bright office"></div>
  <h1 class="hero-title abs">Funding and helping build<br>successful businesses</h1>
  <p class="hero-text abs">This will include a narrative about the target companies, how we work, the type of deals we are interested in, our expectations, etc ...</p>
  <div class="hero-btn abs">Learn more about us
    <svg width="18" height="18" viewBox="0 0 18 18"><circle cx="9" cy="9" r="9" fill="#fff"/><path d="M7 5l4 4-4 4" fill="none" stroke="#222" stroke-width="2.2"/></svg>
  </div>
</section>

<p class="tagline abs"><b>Investments with impact</b> will be the result of engaged, experienced business leaders<br>providing both capital and wisdom to entrepreneurs.</p>

<svg class="route abs" width="706" height="280" viewBox="0 0 706 280">
  <g fill="none" stroke="#555" stroke-dasharray="6 4" stroke-width="1">
    <path d="M10 46 L76 98"/>
    <path d="M392 104 L432 100"/>
    <path d="M634 164 L690 198"/>
  </g>
  <g fill="#222">
    <path d="M8 28a6 6 0 0 1 6 6c0 5-6 11-6 11s-6-6-6-11a6 6 0 0 1 6-6z"/>
    <path d="M698 190a6 6 0 0 1 6 6c0 5-6 11-6 11s-6-6-6-11a6 6 0 0 1 6-6z"/>
  </g>
  <circle cx="8" cy="34" r="2.4" fill="#fff"/><circle cx="698" cy="196" r="2.4" fill="#fff"/>
  <g fill="#d5d5d5"><circle cx="78" cy="58" r="8"/>
    <g stroke="#d5d5d5" stroke-width="2"><path d="M78 44v4M78 68v4M64 58h4M88 58h4M68 48l3 3M85 65l3 3M88 48l-3 3M71 65l-3 3"/></g>
  </g>
  <path d="M436 56a7 7 0 0 1 9-7a9 9 0 0 1 16 2a6 6 0 0 1 2 12h-25a5 5 0 0 1-2-7z" fill="none" stroke="#ccc" stroke-width="2"/>

  <g>
    <ellipse cx="120" cy="182" rx="30" ry="3" fill="#000" opacity=".15"/>
    <circle cx="120" cy="128" r="48" fill="#fff" stroke="#aaa" stroke-dasharray="3 2"/>
    <circle cx="120" cy="128" r="45" fill="#c9ced8" role="img" aria-label="Portrait photograph of a smiling partner in a suit"/>
  </g>
  <g>
    <ellipse cx="232" cy="182" rx="30" ry="3" fill="#000" opacity=".15"/>
    <circle cx="232" cy="128" r="48" fill="#fff" stroke="#aaa" stroke-dasharray="3 2"/>
    <circle cx="232" cy="128" r="45" fill="#e9e4cf" role="img" aria-label="Photograph of a 3D yellow and white pie chart"/>
  </g>
  <g>
    <ellipse cx="344" cy="182" rx="30" ry="3" fill="#000" opacity=".15"/>
    <circle cx="344" cy="128" r="48" fill="#fff" stroke="#aaa" stroke-dasharray="3 2"/>
    <circle cx="344" cy="128" r="45" fill="#b9bdb4" role="img" aria-label="Photograph of a businessman at a laptop with banknotes flying"/>
  </g>

  <ellipse cx="536" cy="248" rx="40" ry="3" fill="#000" opacity=".2"/>
  <circle cx="534" cy="130" r="105" fill="#fff" stroke="#aaa" stroke-dasharray="4 3"/>
  <circle cx="534" cy="130" r="100" fill="#efefef"/>
  <g transform="translate(534 110)">
    <path d="M0 0L0 -57A57 57 0 0 1 54.21 -17.61Z" fill="#f7a70f"/>
    <path d="M0 0L54.21 -17.61A57 57 0 0 1 0 57Z" fill="#fbc446"/>
    <path d="M0 0L0 57A57 57 0 0 1 -54.21 -17.61Z" fill="#fddc94"/>
    <path d="M0 0L-54.21 -17.61A57 57 0 0 1 -36.33 -43.92Z" fill="#8c887b"/>
    <path d="M0 0L-36.33 -43.92A57 57 0 0 1 0 -57Z" fill="#d7d2c6"/>
    <g font-size="7" fill="#333" text-anchor="middle" font-family="Open Sans, sans-serif">
      <text x="22" y="-28">20%</text><text x="31" y="25">30%</text><text x="-31" y="25">30%</text>
      <text x="-31" y="-19">9%</text><text x="-12" y="-34">11%</text>
    </g>
  </g>
  <g font-size="5" fill="#555" font-family="Open Sans, sans-serif">
    <rect x="480" y="179" width="7" height="7" fill="#f7a70f"/><text x="491" y="185">Cash</text>
    <rect x="480" y="189" width="7" height="7" fill="#fbc446"/><text x="491" y="195">NZ Fixed Interest</text>
    <rect x="480" y="199" width="7" height="7" fill="#fddc94"/><text x="491" y="205">World Fixed Interest</text>
    <rect x="550" y="179" width="7" height="7" fill="#8c887b"/><text x="561" y="185">Australasian Shares</text>
    <rect x="550" y="189" width="7" height="7" fill="#d7d2c6"/><text x="561" y="195">World Shares</text>
  </g>
</svg>
<div class="route-label abs" style="left:60px;top:635px">Partner Profiles</div>
<div class="route-label abs" style="left:172px;top:635px">Investment</div>
<div class="route-label abs" style="left:285px;top:635px">Funding application</div>
<div class="route-label abs" style="left:482px;top:700px">Investment profiles</div>

<div class="divider abs"></div>

<h2 class="section-title abs" style="left:70px;top:758px">Latest Blog Posts</h2>
<article class="post abs" style="left:70px;top:798px">
  <div class="post-head"><div class="post-date"><span class="day">09</span><span class="mon">Aug</span></div><h3 class="post-title">Lorem Ipsum is simply dummy text of the</h3></div>
  <p class="post-body">Lorem Ipsum is simply dummy text of the printing and typeset-ting industry. Lorem Ipsum has been the industry's standard dummy text ever since the 1500s, when an unknown printer took a galley of type and scrambled it to make a type specimen book. It has survived not only five centu-</p>
</article>
<article class="post abs" style="left:254px;top:798px">
  <div class="post-head"><div class="post-date"><span class="day">08</span><span class="mon">Aug</span></div><h3 class="post-title">Lorem Ipsum is simply dummy text of the</h3></div>
  <p class="post-body">Lorem Ipsum is simply dummy text of the printing and typeset-ting industry. Lorem Ipsum has been the industry's standard dummy text ever since the 1500s, when an unknown printer took a galley of type and scrambled it to make a type specimen book. It has survived not only five centu-</p>
</article>

<h2 class="section-title abs" style="left:442px;top:758px">Submit a Request</h2>
<form class="request abs">
  <div class="field">Name:</div>
  <div class="field">Email:</div>
  <div class="field msg">Message:</div>
  <div class="submit">SUBMIT</div>
</form>

<footer class="site-footer abs">
  <div class="tab abs">Get In Touch</div>
  <div class="abs" style="left:70px;top:54px">
    <h3 class="foot-title">Links</h3>
    <ul class="foot-links">
      <li>Funding Application</li><li>Invest with Bright Harbor</li><li>Our Process</li>
      <li>Investment Profiles</li><li>Partner Profiles</li><li>News</li>
    </ul>
  </div>
  <div class="abs" style="left:245px;top:54px">
    <h3 class="foot-title">Latest Tweet</h3>
    <div class="tweet"><span class="tweet-icon"><i></i></span><p>Lorem Ipsum is simply dummy text of the printing and typeset-ting industry. Lorem Ipsum has</p></div>
  </div>
  <div class="abs" style="left:422px;top:54px">
    <h3 class="foot-title">Contact Us</h3>
    <ul class="contact-list">
      <li><svg width="6" height="8" viewBox="0 0 6 8"><path d="M3 0a3 3 0 0 1 3 3c0 2-3 5-3 5S0 5 0 3a3 3 0 0 1 3-3z" fill="#888"/></svg><span><b>Address:</b> 1234 Street Name, City Name, United States</span></li>
      <li><svg width="7" height="7" viewBox="0 0 7 7"><path d="M1 0l2 2-1 1a4 4 0 0 0 2 2l1-1 2 2-1 1C3 7 0 4 0 1z" fill="#888"/></svg><span><b>Phone:</b> (123) 456-7890</span></li>
      <li><svg width="8" height="6" viewBox="0 0 8 6"><rect width="8" height="6" fill="#888"/><path d="M0 0l4 3 4-3" stroke="#141414" fill="none"/></svg><span><b>Email:</b> <span class="mail">mail@example.com</span></span></li>
    </ul>
  </div>
  <div class="foot-rule abs"></div>
  <p class="copyright abs">Copyright © 2014 Bright Harbor Capital</p>
</footer>

</body>
</html>
```